Wordpress Web page design with blog & Ecommerce functionality

I need a new Web site for my Learning Consultancy which is based in the U.K. but also works globally.
Catch phrase 'Encouraging empowered contribution'.
Facilitating practical tools and effective communication, organization, problem solving, team/net working and life skills for leaders of today and tomorrow.

I need a website that can be updated easily with ongoing technical support when needed. It needs to have the ability to have a blog, the ability to pay online for courses, books, consultation fees etc.

Target Market(s)

For children/youth, parents, teachers, managers, businesses and organizations everywhere. Tailored or 'off the shelf' solutions for schools, community groups, organizations, government and private businesses. All those who wish to improve their communications, organizational, problem solving, team/networking and life skills.
For example we work in primary, middle & upper schools, community service groups/centres, Leisure Centres, parenting groups, Human resources departments, correctional facilities, motivational speakers groups, private businesses.

Industry/Entity Type

Communication

Font styles to use
Sans Serif

Colors
6b449b
00a990
fbed23
ec2027
0255a3
ffc214

Requirements
Must have
• A professional but open and welcoming front page, which is bright and positive. The theme is for self improvement and team/family/community improvement, so images and colors that represent growth, learning, sharing, cooperation, building, uniting and evolving for example would be important.
• The site needs to be very easy & logical to use. People will come to it to read about the products/courses we offer, want to see outlines and reviews and then look to find dates, locations and pricing for those products and courses.
• It needs to have a billing page that can easily process payments for booked courses/products online and be automated if possible for sending out receipts etc and allow me to keep accurate book keeping for taxes etc.
• A blog were we share tips, articles and links.
• I also need to be able to have links to affiliated pages.
• It needs to be a site that can be added to & updated easily.
• Use my company logo and colour themes.
• I need to have Facebook, twitter, etc LIKE buttons & links also.
• This website is one I like as an example: http://brookvale-kin.org
Nice to have
• A chat feature
• Videos
Should not have
• No black front page. Should not look like every other site. It should not be 'cold' and impersonal but it must also not be frivolous or childlike. It should not be too busy or scant.

```html
<!DOCTYPE html>
<html lang="en">
<head>
<meta charset="utf-8">
<title>Kinwell Learning – Home</title>
<link rel="stylesheet" href="https://fonts.googleapis.com/css2?family=Open+Sans:wght@400;600&family=Dosis:wght@400;500;600&display=swap">
<style>
:root{
  --red:#cc2229;
  --green:#16a78b;
  --yellow:#ffc214;
  --purple:#5b1f73;
  --text:#555;
  --muted:#8a8a8a;
  --line:#dcdcdc;
  --footer:#f5f6f7;
  --white:#fff;
}
*{box-sizing:border-box;margin:0;padding:0}
html,body{width:1200px;height:2362px;overflow:hidden;background:var(--white)}
body{font-family:"Open Sans",Arial,sans-serif;color:var(--text);position:relative}
.wrap{width:962px;margin:0 auto;position:relative}
a{color:inherit;text-decoration:none}

/* header */
.site-header{height:178px}
.top-bar{height:112px;border-bottom:1px solid var(--line);display:flex;align-items:center;justify-content:space-between}
.brand{display:flex;align-items:center;gap:14px}
.brand-dot{width:52px;height:52px;border-radius:50%;background:var(--purple)}
.brand-name{font-size:30px;font-weight:600;color:var(--purple)}
.top-tools{display:flex;align-items:center;gap:18px}
.social{display:flex;gap:8px}
.social span{width:32px;height:32px;border-radius:50%;display:block}
.search{width:220px;height:38px;background:#eeeeee;display:flex;align-items:center;justify-content:space-between;padding:0 14px;font-size:14px;color:#777}
.cart{width:52px;height:52px;border:2px solid var(--purple);border-radius:50%;position:relative;display:flex;align-items:center;justify-content:center}
.cart-count{position:absolute;top:-8px;right:-4px;width:22px;height:22px;border-radius:50%;background:var(--red);color:#fff;font-size:12px;display:flex;align-items:center;justify-content:center}
.main-nav{height:66px;display:flex;align-items:center;justify-content:space-between;padding:0 26px;font-size:15px;color:#777;text-transform:uppercase}
.main-nav .active{color:var(--red)}

/* hero */
.hero{height:524px;position:relative;background:linear-gradient(135deg,#e9dccb 0%,#d7b893 40%,#c98f5e 75%,#b47a4a 100%)}
.hero-arrow{position:absolute;top:241px;width:34px;height:34px;background:#555;display:flex;align-items:center;justify-content:center}
.hero-arrow.left{left:0}.hero-arrow.right{right:0}
.hero-caption{position:absolute;left:50%;top:384px;transform:translateX(-50%);background:rgba(255,255,255,.92);padding:8px 16px;font-size:25px;font-weight:600;color:#333;letter-spacing:.5px;white-space:nowrap}

/* welcome */
.welcome{padding-top:72px;text-align:center}
.welcome h1{font-weight:400;font-size:32px;color:var(--red);margin-bottom:22px}
.welcome p{font-size:15.5px;line-height:26px;color:var(--muted);padding:0 30px}

/* products */
.products{display:flex;gap:17px;margin-top:52px}
.product{width:228px;height:293px;border:1px solid #cfe3dd}
.product-cover{height:178px}
.product-info{height:115px;background:var(--green);color:#fff;text-align:center;padding-top:10px}
.product-title{font-family:"Dosis",sans-serif;font-weight:500;font-size:23px;letter-spacing:.3px}
.product-sub{font-family:"Dosis",sans-serif;font-size:16px;margin-top:2px}
.product-buy{display:flex;justify-content:center;align-items:center;gap:26px;margin-top:10px}
.price{font-family:"Dosis",sans-serif;font-size:21px}
.pay{background:var(--yellow);color:#333;font-size:13px;font-weight:600;padding:7px 18px}

/* services */
.services{display:flex;gap:22px;margin-top:58px}
.video{width:474px;height:293px;position:relative;background:linear-gradient(160deg,#c9c2b6,#8e8577 60%,#6b6357)}
.video-bar{position:absolute;left:0;right:0;bottom:0;height:30px;background:rgba(20,20,20,.8)}
.video-progress{position:absolute;left:22px;bottom:12px;width:320px;height:5px;background:#555}
.video-progress i{display:block;width:150px;height:5px;background:#2aa2dc}
.play{position:absolute;left:50%;top:50%;transform:translate(-50%,-50%);width:38px;height:30px;background:rgba(0,0,0,.6);display:flex;align-items:center;justify-content:center}
.services-text{flex:1;padding-top:0}
.services-text h2{font-family:"Dosis",sans-serif;font-weight:500;font-size:36px;color:var(--red);line-height:40px}
.services-text p{font-size:14px;line-height:24px;color:#666;margin-top:14px}
.service-list{list-style:none;margin-top:14px}
.service-list li{display:flex;align-items:center;gap:16px;font-size:15px;color:#444;height:41px}

/* blog */
.blog{margin-top:68px}
.blog h2{font-family:"Dosis",sans-serif;font-weight:500;font-size:32px;color:#333}
.posts{display:flex;gap:56px;margin-top:20px}
.post{display:flex;gap:18px;width:453px}
.post-img{width:220px;height:173px;flex:none}
.post-body{flex:1}
.post-title{font-family:"Dosis",sans-serif;font-size:18px;color:#333;padding-bottom:14px;border-bottom:1px solid var(--line)}
.post-meta{font-size:12.5px;color:#666;margin-top:12px}
.post-excerpt{font-size:13.5px;line-height:21px;color:var(--muted);margin-top:14px}
.read-more{font-size:12px;color:var(--red);margin-top:10px;display:block}

/* footer */
.site-footer{position:absolute;left:0;right:0;top:1989px;height:244px;background:var(--footer)}
.footer-cols{display:flex;height:244px}
.footer-col{padding-top:30px}
.footer-col + .footer-col{border-left:1px solid #e4e4e4}
.col-testi{width:352px;padding-right:30px}
.col-connect{width:338px;padding-left:58px}
.col-contact{flex:1;padding-left:44px}
.footer-col h3{font-weight:400;font-size:16px;color:var(--red);margin-bottom:18px}
.quote{font-size:13.5px;line-height:21px;color:#666}
.stars{color:var(--yellow);font-size:14px;margin-top:10px;letter-spacing:1px}
.ago{font-size:13px;color:#777;margin-top:6px}
.follow{display:inline-block;border:1px solid #c6cdd6;border-radius:3px;background:#eef1f4;font-size:12px;color:#333;padding:2px 8px;margin-bottom:8px}
.follow-count{display:inline-block;border:1px solid #c6cdd6;font-size:11px;padding:1px 6px;margin-left:6px;color:#2a6fa8}
.footer-brand{display:flex;align-items:center;gap:10px;margin-top:28px}
.footer-brand span{width:36px;height:36px;border-radius:50%;background:var(--purple)}
.footer-brand b{font-weight:600;font-size:19px;color:var(--purple)}
.address{font-size:14.5px;line-height:24px;color:#555}
.contact-line{display:flex;align-items:center;gap:18px;font-size:14px;color:#555;margin-top:14px}
.bottom-bar{position:absolute;left:0;right:0;top:2233px;height:129px;background:var(--purple);color:#fff}
.bottom-inner{width:962px;margin:0 auto;position:relative;padding-top:36px}
.bottom-nav{font-size:13.5px;padding-bottom:14px;border-bottom:1px solid rgba(255,255,255,.35);width:648px}
.bottom-nav span{margin:0 8px}
.copyright{font-size:12.5px;margin-top:16px}
.bottom-icons{position:absolute;right:0;top:32px;display:flex;gap:12px}
.bottom-icons span{width:36px;height:36px;border:2px solid #fff;border-radius:50%;display:flex;align-items:center;justify-content:center}
</style>
</head>
<body>

<header class="site-header">
  <div class="wrap">
    <div class="top-bar">
      <div class="brand"><span class="brand-dot"></span><span class="brand-name">Kinwell Learning</span></div>
      <div class="top-tools">
        <div class="social" aria-label="Social links">
          <span style="background:#3b5a9a"></span>
          <span style="background:#2aa7e0"></span>
          <span style="background:#444"></span>
          <span style="background:#f07a22"></span>
          <span style="background:#d9272e"></span>
        </div>
        <div class="search">Search
          <svg width="16" height="16" viewBox="0 0 16 16"><circle cx="6.5" cy="6.5" r="5" fill="none" stroke="#555" stroke-width="2"/><line x1="10" y1="10" x2="15" y2="15" stroke="#555" stroke-width="2"/></svg>
        </div>
        <div class="cart">
          <svg width="22" height="20" viewBox="0 0 22 20"><path d="M1 2h4l3 11h10l3-8H7" fill="none" stroke="#5b1f73" stroke-width="2"/><circle cx="9" cy="17" r="1.8" fill="#5b1f73"/><circle cx="17" cy="17" r="1.8" fill="#5b1f73"/></svg>
          <span class="cart-count">0</span>
        </div>
      </div>
    </div>
    <nav class="main-nav">
      <a class="active">Home</a><a>About Us</a><a>Services</a><a>Classes</a><a>Events</a><a>Gallery</a><a>Contact Us</a><a>Get Started Now</a>
    </nav>
  </div>
</header>

<section class="hero" role="img" aria-label="Children sitting on a classroom floor building with wooden letter blocks">
  <span class="hero-arrow left"><svg width="16" height="14" viewBox="0 0 16 14"><path d="M15 7H2M7 1L1 7l6 6" fill="none" stroke="#fff" stroke-width="2.5"/></svg></span>
  <span class="hero-arrow right"><svg width="16" height="14" viewBox="0 0 16 14"><path d="M1 7h13M9 1l6 6-6 6" fill="none" stroke="#fff" stroke-width="2.5"/></svg></span>
  <div class="hero-caption">ENCOURAGING EMPOWERED CONTRIBUTION</div>
</section>

<main class="wrap">
  <section class="welcome">
    <h1>Welcome to Kinwell Learning</h1>
    <p>Fusce sollicitudin lorem et luctus volutpat. Proin placerat dapibus gravida. In tristique tristique nulla eget hendrerit. Maecenas vel tortor accumsan quam varius imperdiet vel eget elit. Aenean facilisis tincidunt lectus, id dictum nisi luctus eget. Vivamus efficitur ex condimentum, malesuada eros eget, feugiat nibh. Sed tellus ex, imperdiet eget gravida sit amet, volutpat eget turpis. In nec ultricies est. Etiam mattis augue vehicula odio posuere, sit amet tempus lectus luctus.</p>
  </section>

  <section class="products">
    <article class="product">
      <div class="product-cover" role="img" aria-label="Book cover with a parent hugging a child" style="background:linear-gradient(90deg,#d9c3a8 0%,#e8dccd 45%,#f7f7f7 46%)"></div>
      <div class="product-info"><div class="product-title">CALM GUIDANCE</div><div class="product-sub">Multi-media Units</div>
        <div class="product-buy"><span class="price">£15.30</span><a class="pay">PAY NOW</a></div></div>
    </article>
    <article class="product">
      <div class="product-cover" role="img" aria-label="Book cover with schoolchildren and coloured stripes" style="background:linear-gradient(180deg,#f2eee4 0%,#e9e2d4 70%,#3ab0b8 71%)"></div>
      <div class="product-info"><div class="product-title">CALM GUIDANCE</div><div class="product-sub">In The Classroom</div>
        <div class="product-buy"><span class="price">£15.30</span><a class="pay">PAY NOW</a></div></div>
    </article>
    <article class="product">
      <div class="product-cover" role="img" aria-label="Book cover with teenagers and coloured stripes" style="background:linear-gradient(180deg,#f3efe6 0%,#e6e0d4 70%,#a7c83a 71%)"></div>
      <div class="product-info"><div class="product-title">CALM GUIDANCE</div><div class="product-sub">For Teenagers</div>
        <div class="product-buy"><span class="price">£15.30</span><a class="pay">PAY NOW</a></div></div>
    </article>
    <article class="product">
      <div class="product-cover" role="img" aria-label="Book cover with a preschool child and coloured stripes" style="background:linear-gradient(180deg,#f6efe6 0%,#f0d9c0 70%,#1fb0c8 71%)"></div>
      <div class="product-info"><div class="product-title">CALM GUIDANCE</div><div class="product-sub">For Preschoolers</div>
        <div class="product-buy"><span class="price">£15.30</span><a class="pay">PAY NOW</a></div></div>
    </article>
  </section>

  <section class="services">
    <div class="video" role="img" aria-label="Video of a teacher reading to a class of children">
      <span class="play"><svg width="12" height="14" viewBox="0 0 12 14"><path d="M1 1l10 6-10 6z" fill="#fff"/></svg></span>
      <div class="video-bar"></div>
      <div class="video-progress"><i></i></div>
    </div>
    <div class="services-text">
      <h2>Our Services</h2>
      <p>Lorem ipsum dolor sit amet, consectetur adipisicing elit, sed do eiusmod tempor incididunt ut labore et dolore magna aliqua. Ut enim ad minim veniam Sed condimentum placerat vulputate.</p>
      <ul class="service-list">
        <li><svg width="14" height="12" viewBox="0 0 14 12"><path d="M1 6l4 4 8-9" fill="none" stroke="#cc2229" stroke-width="2.5"/></svg>Pellentesque tincidunt rutrum.</li>
        <li><svg width="14" height="12" viewBox="0 0 14 12"><path d="M1 6l4 4 8-9" fill="none" stroke="#cc2229" stroke-width="2.5"/></svg>Calm Guidance</li>
        <li><svg width="14" height="12" viewBox="0 0 14 12"><path d="M1 6l4 4 8-9" fill="none" stroke="#cc2229" stroke-width="2.5"/></svg>Lorem ipsum dolor amet, consectetur adipiscing</li>
        <li><svg width="14" height="12" viewBox="0 0 14 12"><path d="M1 6l4 4 8-9" fill="none" stroke="#cc2229" stroke-width="2.5"/></svg>Pellentesque tincidunt rutrum.</li>
      </ul>
    </div>
  </section>

  <section class="blog">
    <h2>OUR BLOG</h2>
    <div class="posts">
      <article class="post">
        <div class="post-img" role="img" aria-label="Children playing with blocks in a classroom" style="background:linear-gradient(150deg,#e9e1d2,#c7a27a 60%,#8d6a4c)"></div>
        <div class="post-body">
          <div class="post-title">NIBH EUISMOD TINCIDUNT UT</div>
          <div class="post-meta">by admin June 26, 2014 &nbsp; 0 &nbsp; 1</div>
          <p class="post-excerpt">Lorem ipsum dolor sit amet, consectetur adipisc elit. Sed blandit massa vel mauris sollicitudin dig issim.</p>
          <a class="read-more">READ MORE +</a>
        </div>
      </article>
      <article class="post">
        <div class="post-img" role="img" aria-label="Smiling schoolchildren at a desk with coloured pencils" style="background:linear-gradient(150deg,#e8eef2,#c9dbe6 55%,#4aa6d6)"></div>
        <div class="post-body">
          <div class="post-title">NIBH EUISMOD TINCIDUNT UT</div>
          <div class="post-meta">by admin June 26, 2014 &nbsp; 0 &nbsp; 1</div>
          <p class="post-excerpt">Lorem ipsum dolor sit amet, consectetur adipisc elit. Sed blandit massa vel mauris sollicitudin dig issim.</p>
          <a class="read-more">READ MORE +</a>
        </div>
      </article>
    </div>
  </section>
</main>

<footer class="site-footer">
  <div class="wrap footer-cols">
    <div class="footer-col col-testi">
      <h3>TESTIMONIALS</h3>
      <p class="quote">“ Nulla sollicitudin tincidunt dui et egestas. Phasellus non sem tum, ullamcorper vitae, accumsan dui. Duis dignissim condi lorem. ”</p>
      <div class="stars">★★★☆☆</div>
      <div class="ago">8 Months Ago</div>
    </div>
    <div class="footer-col col-connect">
      <h3>CONNECT WITH US</h3>
      <div><span class="follow">Follow @kinwelllearn</span></div>
      <div><span class="follow">Follow</span><span class="follow-count">105</span></div>
      <div class="footer-brand"><span></span><b>Kinwell Learning</b></div>
    </div>
    <div class="footer-col col-contact">
      <h3>CONTACT US</h3>
      <p class="address">27 Alder Row, Suite 12<br>Marlow Heath, MH4 2QT</p>
      <div class="contact-line"><svg width="20" height="20" viewBox="0 0 20 20"><path d="M4 2l3 4-2 2c1 3 3 5 6 6l2-2 4 3-2 3C8 18 2 12 2 4z" fill="none" stroke="#6a7c94" stroke-width="1.4"/></svg>1.555-014-2290</div>
      <div class="contact-line"><svg width="20" height="16" viewBox="0 0 20 16"><rect x="1" y="1" width="18" height="14" fill="none" stroke="#6a7c94" stroke-width="1.4"/><path d="M1 1l9 8 9-8" fill="none" stroke="#6a7c94" stroke-width="1.4"/></svg>info@kinwell-learning.org</div>
    </div>
  </div>
</footer>

<div class="bottom-bar">
  <div class="bottom-inner">
    <div class="bottom-nav">Home<span>|</span>About us<span>|</span>Services<span>|</span>Classes<span>|</span>Events<span>|</span>Gallery<span>|</span>Contact us<span>|</span>Get Started Now</div>
    <div class="copyright">Copyright © 2015 Kinwell Learning. &nbsp; All rights reserved.</div>
    <div class="bottom-icons">
      <span><svg width="16" height="12" viewBox="0 0 16 12"><rect x="1" y="1" width="14" height="10" fill="none" stroke="#fff" stroke-width="1.5"/><path d="M1 1l7 6 7-6" fill="none" stroke="#fff" stroke-width="1.5"/></svg></span>
      <span><svg width="14" height="16" viewBox="0 0 14 16"><path d="M7 15V2M1 8l6-6 6 6" fill="none" stroke="#fff" stroke-width="1.8"/></svg></span>
    </div>
  </div>
</div>

</body>
</html>
```